Custom Office Whiteboard for Staff

I need a custom whiteboard layout design. All fields are contained in the attached images along with artwork requirements including required bleed. Size will be 1200mm x 900mm.

Feel free to make is more visually appealing than this draft.

Use colors blue, black and white to keep company feel.

Font styles to use
Sans Serif

Colors
ffffff
000000
33a6d7

```html
<!DOCTYPE html>
<html lang="en">
<head>
<meta charset="utf-8">
<title>Lofty Ballooning – Staff Whiteboard</title>
<link href="https://fonts.googleapis.com/css2?family=Fira+Sans+Condensed:wght@500;600;700&display=swap" rel="stylesheet">
<style>
  :root {
    --blue: #33a6d7;
    --black: #1b1b1b;
    --white: #ffffff;
    --row-tint: #e7f4fb;
    --rule: #c6e2f1;
    --frame: #2a2a2a;
  }
  * { box-sizing: border-box; margin: 0; padding: 0; }
  html, body { width: 1200px; height: 900px; overflow: hidden; background: var(--white); }
  body { position: relative; font-family: "Fira Sans Condensed", "Arial Narrow", sans-serif; color: var(--black); }

  .masthead {
    position: absolute; left: 36px; top: 36px; width: 1128px; height: 115px;
    background: var(--black); display: flex; align-items: center; justify-content: space-between;
    padding: 0 20px 0 28px;
  }
  .masthead-rule { position: absolute; left: 36px; top: 156px; width: 1128px; height: 2px; background: var(--blue); }
  .brand { display: flex; align-items: center; gap: 14px; color: var(--blue); font-weight: 700; font-size: 52px; letter-spacing: 1px; }
  .brand-dot { width: 34px; height: 34px; border-radius: 50%; background: var(--blue); }
  .company { text-align: right; color: var(--white); font-weight: 600; }
  .company-name { color: var(--blue); font-size: 31px; line-height: 1.1; margin-bottom: 6px; }
  .company-line { font-size: 16px; line-height: 1.45; }

  .panel { position: absolute; border: 1.5px solid var(--frame); border-radius: 9px; }
  .panel-title {
    position: absolute; top: -17px; left: 50%; transform: translateX(-50%);
    background: var(--white); padding: 0 10px; white-space: nowrap;
    font-size: 25px; font-weight: 600; display: flex; align-items: center; gap: 8px; line-height: 32px;
  }
  .panel-title::before { content: ""; width: 15px; height: 15px; border-radius: 50%; background: var(--blue); }

  .crew { left: 36px; top: 201px; width: 824px; height: 369px; }
  .notes { left: 870px; top: 201px; width: 295px; height: 369px; }
  .six { left: 36px; top: 595px; width: 297px; height: 269px; }
  .twelve { left: 343px; top: 595px; width: 297px; height: 269px; }
  .fleet { left: 648px; top: 595px; width: 517px; height: 269px; }

  .grid { position: absolute; left: 9px; right: 9px; top: 21px; border-collapse: collapse; table-layout: fixed; }
  .grid th {
    background: var(--blue); color: var(--white); font-weight: 600; font-size: 13px; line-height: 1.05;
    text-align: center; vertical-align: bottom; padding: 0 6px 5px; border-bottom: 3px double var(--white);
    box-shadow: inset 0 -1px 0 var(--blue);
  }
  .grid th:first-child, .grid td:first-child { text-align: left; }
  .grid td { font-size: 13px; font-weight: 600; padding: 0 6px; white-space: nowrap; }
  .grid td + td, .grid th + th { border-left: 1.5px solid var(--rule); }
  .grid th + th { border-left-color: var(--white); }
  .grid tbody tr:nth-child(even) td { background: var(--row-tint); }
  .grid td.c { text-align: center; }

  .crew .grid thead tr { height: 36px; }
  .crew .grid tbody tr { height: 25.2px; }
  .small .grid thead tr { height: 38px; }
  .small .grid tbody tr { height: 24.5px; }
</style>
</head>
<body>
  <header class="masthead">
    <div class="brand"><span class="brand-dot"></span>Lofty Ballooning</div>
    <div class="company">
      <div class="company-name">Skyward Envelopes Pty Ltd T/A Lofty Ballooning</div>
      <div class="company-line">CASA AOC: S512098,&nbsp; Certificate of Approval: 4816</div>
      <div class="company-line">info@loftyballooning.com.au,&nbsp; www.loftyballooning.com.au, phone 1300 555 019</div>
    </div>
  </header>
  <div class="masthead-rule"></div>

  <section class="panel crew">
    <h2 class="panel-title">Flight / Ground Crew</h2>
    <table class="grid">
      <colgroup>
        <col style="width:147px"><col style="width:82px"><col style="width:72px"><col style="width:68px"><col style="width:83px"><col style="width:82px"><col style="width:82px"><col style="width:106px"><col style="width:78px">
      </colgroup>
      <thead><tr><th>Crew Name</th><th>License<br>Class</th><th>Medical</th><th>BFR</th><th>Instructor<br>Rating</th><th>CAO 20.11</th><th>DAMP</th><th>Maintenance<br>Authority</th><th>ASIC</th></tr></thead>
      <tbody>
        <tr><td></td><td></td><td></td><td></td><td></td><td></td><td></td><td></td><td></td></tr>
        <tr><td></td><td></td><td></td><td></td><td></td><td></td><td></td><td></td><td></td></tr>
        <tr><td></td><td></td><td></td><td></td><td></td><td></td><td></td><td></td><td></td></tr>
        <tr><td></td><td></td><td></td><td></td><td></td><td></td><td></td><td></td><td></td></tr>
        <tr><td></td><td></td><td></td><td></td><td></td><td></td><td></td><td></td><td></td></tr>
        <tr><td></td><td></td><td></td><td></td><td></td><td></td><td></td><td></td><td></td></tr>
        <tr><td></td><td></td><td></td><td></td><td></td><td></td><td></td><td></td><td></td></tr>
        <tr><td></td><td></td><td></td><td></td><td></td><td></td><td></td><td></td><td></td></tr>
        <tr><td></td><td></td><td></td><td></td><td></td><td></td><td></td><td></td><td></td></tr>
        <tr><td></td><td></td><td></td><td></td><td></td><td></td><td></td><td></td><td></td></tr>
        <tr><td></td><td></td><td></td><td></td><td></td><td></td><td></td><td></td><td></td></tr>
        <tr><td></td><td></td><td></td><td></td><td></td><td></td><td></td><td></td><td></td></tr>
      </tbody>
    </table>
  </section>

  <section class="panel notes">
    <h2 class="panel-title">NOTES</h2>
  </section>

  <section class="panel small six">
    <h2 class="panel-title">6 Monthly Tasks</h2>
    <table class="grid">
      <colgroup><col style="width:160px"><col></colgroup>
      <thead><tr><th>Task</th><th>Due Date</th></tr></thead>
      <tbody>
        <tr><td>Operations Manual</td><td></td></tr>
        <tr><td>Staff Meeting</td><td></td></tr>
        <tr><td>SMS Meeting</td><td></td></tr>
        <tr><td>Fire Extinguisher Inspection</td><td></td></tr>
        <tr><td>Flight Instrument Inspection</td><td></td></tr>
        <tr><td></td><td></td></tr>
        <tr><td></td><td></td></tr>
        <tr><td></td><td></td></tr>
      </tbody>
    </table>
  </section>

  <section class="panel small twelve">
    <h2 class="panel-title">12 Monthly Tasks</h2>
    <table class="grid">
      <colgroup><col style="width:160px"><col></colgroup>
      <thead><tr><th>Task</th><th>Due Date</th></tr></thead>
      <tbody>
        <tr><td>COA Internal Audit</td><td></td></tr>
        <tr><td>SMS Audit</td><td></td></tr>
        <tr><td>Fatigue Training</td><td></td></tr>
        <tr><td>CAO 20.11</td><td></td></tr>
        <tr><td></td><td></td></tr>
        <tr><td></td><td></td></tr>
        <tr><td></td><td></td></tr>
        <tr><td></td><td></td></tr>
      </tbody>
    </table>
  </section>

  <section class="panel small fleet">
    <h2 class="panel-title">Balloon Annual / Periodic Schedule</h2>
    <table class="grid">
      <colgroup><col style="width:100px"><col style="width:118px"><col style="width:146px"><col></colgroup>
      <thead><tr><th>Balloon</th><th>Type</th><th>Annual Date</th><th>Periodic Time</th></tr></thead>
      <tbody>
        <tr><td>VH-QLA</td><td class="c">Avr D90</td><td></td><td></td></tr>
        <tr><td>VH-QLB</td><td class="c">Avr E180</td><td></td><td></td></tr>
        <tr><td>VH-QLC</td><td class="c">Avr E240</td><td></td><td></td></tr>
        <tr><td>VH-QLD</td><td class="c">Avr B400</td><td></td><td></td></tr>
        <tr><td>VH-QLE</td><td class="c">Avr G450</td><td></td><td></td></tr>
        <tr><td></td><td></td><td></td><td></td></tr>
        <tr><td></td><td></td><td></td><td></td></tr>
        <tr><td></td><td></td><td></td><td></td></tr>
      </tbody>
    </table>
  </section>
</body>
</html>
```